French Puns

Creation of a cover for a book on French plays on words.
The public is lovers of the French language
TITLE: The gentle phrases of Honoré Vasseline
SUB-TITLE: Witty words, wit of words
PUBLISHER (at the bottom of the page): Editions Plumeau
(See joined examples, previous books of the same author)
Size: 14 x 20.5 cm
Please note that the text on the cover is in French, not in English:
Fine phrases from Honoré Vasseline
Witty words, witty words (subtitle, smaller)
Plumeau Editions

```html
<!DOCTYPE html>
<html lang="fr">
<head>
<meta charset="utf-8">
<title>Les bons mots d'Honoré Vasseline</title>
<link rel="stylesheet" href="https://fonts.googleapis.com/css2?family=Lobster&family=Macondo&family=Lato:ital,wght@0,700;1,400&display=swap">
<style>
  :root {
    --page: #ffffff;
    --cover: #ebeae1;
    --teal: #07625f;
    --navy: #0b2556;
    --ink: #4a4a48;
    --art-light: #e4e3d9;
    --art-dark: #d9d8cd;
  }
  html, body {
    margin: 0;
    width: 1200px;
    height: 1200px;
    overflow: hidden;
    background: var(--page);
  }
  .book-cover {
    position: absolute;
    left: 224px;
    top: 50px;
    width: 751px;
    height: 1100px;
    background: var(--cover);
    text-align: center;
  }
  .book-cover > * {
    position: absolute;
    left: 0;
    right: 0;
    margin: 0;
  }
  .author {
    top: 52px;
    font-family: "Lato", sans-serif;
    font-weight: 700;
    font-size: 33px;
    letter-spacing: 0.26em;
    color: var(--ink);
  }
  .title {
    top: 165px;
    font-family: "Lobster", cursive;
    font-weight: 400;
    font-size: 124px;
    line-height: 125px;
    color: var(--teal);
  }
  .title-author {
    top: 428px;
    font-family: "Macondo", serif;
    font-size: 56px;
    color: var(--navy);
  }
  .subtitle {
    top: 568px;
    font-family: "Lato", sans-serif;
    font-style: italic;
    font-size: 35px;
    color: var(--ink);
  }
  .cover-art {
    left: 215px;
    right: auto;
    top: 690px;
    width: 310px;
    height: 195px;
    border-radius: 12px;
    background: radial-gradient(ellipse at center, var(--art-dark), var(--art-light));
  }
  .publisher {
    top: 1000px;
    font-family: "Lato", sans-serif;
    font-weight: 700;
    font-size: 31px;
    letter-spacing: 0.25em;
    color: var(--ink);
  }
</style>
</head>
<body>
  <main class="book-cover">
    <p class="author">HONORÉ VASSELINE</p>
    <h1 class="title">LES BONS<br>MOTS</h1>
    <p class="title-author">d’Honoré Vasseline</p>
    <p class="subtitle">Mots d'esprit, esprit des mots</p>
    <div class="cover-art" role="img" aria-label="Dessin d'un sourire espiègle avec un clin d'œil et une langue aux couleurs bleu, blanc, rouge"></div>
    <p class="publisher">EDITIONS PLUMEAU</p>
  </main>
</body>
</html>
```